Sliders required for launch-to-market of broadband & telecoms provider

We require first of many sliders for launch-to-market of broadband & telecoms provider. We are looking for a unique colour scheme with high quality graphics. Please see attached images as to what we are looking for. We like the angled look as on banner image, but want a more brighter colour scheme. Glossy & hi res...

Industry/Entity Type

Telecommunications

Number of Pages Required

1 page

Colors

Designer to choose colors to be used in the design.

Requirements
Must have
• unique colour scheme and hi res images
Nice to have
• We like the angled look as on banner image, but want a more brighter/richer individual colour scheme. Glossy & hi res... as the colour will be our main colour used across site so can't just be standard colour. It needs to be unique to our brand.
Should not have
• boring colour scheme and low quality images

```html
<!DOCTYPE html>
<html lang="en">
<head>
<meta charset="utf-8">
<title>Home Broadband Slider</title>
<link rel="stylesheet" href="https://fonts.googleapis.com/css2?family=Montserrat:wght@400&display=swap">
<style>
  :root {
    --page-bg: #fdfdfd;
    --berry-light: #8d1a3b;
    --berry-mid: #6a0734;
    --berry-dark: #3e0719;
    --silver-light: #f6f6f7;
    --silver-dark: #e5e5e7;
    --label-ink: #444446;
  }
  html, body {
    margin: 0;
    padding: 0;
    width: 1200px;
    height: 1000px;
    overflow: hidden;
    background: var(--page-bg);
  }
  .slider {
    position: absolute;
    left: 155px;
    top: 217px;
    width: 891px;
    height: 569px;
    box-shadow: 0 1px 3px rgba(0, 0, 0, 0.12);
    overflow: hidden;
  }
  .slider-art {
    position: absolute;
    inset: 0;
    display: block;
  }
  .slider-label {
    position: absolute;
    right: 37px;
    top: 518px;
    margin: 0;
    font-family: "Montserrat", sans-serif;
    font-weight: 400;
    font-size: 16.5px;
    line-height: 1;
    letter-spacing: 0.2px;
    color: var(--label-ink);
  }
</style>
</head>
<body>
  <section class="slider">
    <svg class="slider-art" width="891" height="569" viewBox="0 0 891 569" aria-hidden="true">
      <defs>
        <radialGradient id="silver-sheen" cx="230" cy="390" r="620" gradientUnits="userSpaceOnUse">
          <stop offset="0" style="stop-color: var(--silver-light)"/>
          <stop offset="0.7" style="stop-color: var(--silver-dark)"/>
          <stop offset="1" style="stop-color: var(--silver-dark)"/>
        </radialGradient>
        <linearGradient id="berry-band" x1="0" y1="0" x2="891" y2="0" gradientUnits="userSpaceOnUse">
          <stop offset="0" style="stop-color: var(--berry-light)"/>
          <stop offset="0.55" style="stop-color: var(--berry-mid)"/>
          <stop offset="0.8" style="stop-color: var(--berry-dark)"/>
          <stop offset="1" style="stop-color: var(--berry-dark)"/>
        </linearGradient>
        <radialGradient id="berry-glow" cx="0" cy="0" r="420" gradientUnits="userSpaceOnUse">
          <stop offset="0" stop-color="#9a1f3c" stop-opacity="0.55"/>
          <stop offset="1" stop-color="#9a1f3c" stop-opacity="0"/>
        </radialGradient>
      </defs>
      <rect class="slider-base" width="891" height="569" fill="url(#silver-sheen)"/>
      <polygon class="slider-band" points="0,0 891,0 891,223 0,363" fill="url(#berry-band)"/>
      <polygon class="slider-band-glow" points="0,0 891,0 891,223 0,363" fill="url(#berry-glow)"/>
    </svg>
    <p class="slider-label">HOME BROADBAND</p>
  </section>
</body>
</html>
```